Business Card and Word .doc header and footer required

I need a business card designed for my cybersecurity consulting company. Also required, is a header and footer to be ued for my word documents.
Attached is the Logo design, font and rgb used.

Industry/Entity Type

Cyber Security Consulting

Contact Information for Business Card

Name, Phone, email, website

Colors
0054AA
0677BA
7BADD7
CADEEF
E8F1F8

Requirements
Must have
• Sleek, modern

```html
<!DOCTYPE html>
<html lang="en">
<head>
<meta charset="utf-8">
<title>Harlow Ridge Consulting – Business Card</title>
<link href="https://fonts.googleapis.com/css2?family=Montserrat:wght@400;500;600;700&display=swap" rel="stylesheet">
<style>
  :root {
    --blue-deep: #0054AA;
    --blue-mid: #0677BA;
    --blue-soft: #7BADD7;
    --blue-pale: #CADEEF;
    --blue-mist: #E8F1F8;
    --navy: #0A1220;
    --ink: #0D1A2B;
    --white: #FFFFFF;
    --backdrop: #EEF1F4;
  }
  * { box-sizing: border-box; margin: 0; padding: 0; }
  html, body { width: 1200px; height: 960px; overflow: hidden; }
  body {
    background: var(--backdrop);
    font-family: "Montserrat", sans-serif;
    position: relative;
  }
  .card {
    position: absolute;
    width: 560px;
    height: 320px;
    border-radius: 18px;
    overflow: hidden;
    box-shadow: 0 10px 28px rgba(10, 18, 32, 0.18);
  }
  .card-back { left: 70px; top: 90px; }
  .card-front { left: 570px; top: 550px; background: var(--white); }

  /* Back side */
  .back-pattern {
    position: absolute; inset: 0;
    background:
      radial-gradient(circle at 45% 40%, rgba(123, 173, 215, 0.55) 0%, rgba(123, 173, 215, 0) 55%),
      linear-gradient(160deg, #1E86C2 0%, var(--blue-mid) 55%, #0A6BA6 100%);
  }
  .back-brand {
    position: absolute;
    right: 40px; top: 120px;
    display: flex; align-items: center; gap: 10px;
    color: var(--white);
    font-weight: 700; font-size: 16px; letter-spacing: 1px;
  }
  .back-brand .dot {
    width: 12px; height: 12px; border-radius: 50%;
    background: var(--white);
  }

  /* Front side */
  .front-art { position: absolute; inset: 0; }
  .front-art .panel-navy { fill: var(--navy); }
  .front-art .stripe-mid { fill: var(--blue-mid); }
  .front-art .stripe-deep { fill: var(--blue-deep); }
  .brand {
    position: absolute;
    left: 30px; top: 138px;
    width: 290px;
    text-align: center;
    color: var(--ink);
  }
  .brand-name {
    font-weight: 700; font-size: 26px; letter-spacing: 0.5px; line-height: 1;
  }
  .brand-sub {
    display: flex; align-items: center; justify-content: center; gap: 8px;
    margin-top: 9px;
    color: var(--blue-mid);
    font-weight: 500; font-size: 10px; letter-spacing: 5px;
  }
  .brand-sub::before, .brand-sub::after {
    content: ""; width: 22px; height: 1.5px; background: var(--blue-mid);
  }
  .contact {
    position: absolute;
    right: 28px; top: 120px;
    width: 160px;
    text-align: right;
    color: var(--white);
  }
  .person-name { font-weight: 500; font-size: 17px; letter-spacing: 0.5px; white-space: nowrap; }
  .person-role { color: var(--blue-mid); font-size: 11px; margin-top: 2px; }
  .contact-list { list-style: none; margin-top: 20px; }
  .contact-list li {
    display: flex; justify-content: flex-end; align-items: center; gap: 7px;
    font-size: 10.5px; line-height: 1.8; white-space: nowrap;
  }
  .contact-list svg { width: 10px; height: 10px; fill: var(--blue-mid); flex: none; }
</style>
</head>
<body>

  <section class="card card-back" aria-label="Card back">
    <div class="back-pattern" role="img" aria-label="Repeating faint brand pattern on blue"></div>
    <div class="back-brand"><span class="dot"></span>HARLOW RIDGE</div>
  </section>

  <section class="card card-front" aria-label="Card front">
    <svg class="front-art" viewBox="0 0 560 320" aria-hidden="true">
      <defs>
        <linearGradient id="mistFade" x1="0" y1="0" x2="0.6" y2="1">
          <stop offset="0" stop-color="#FFFFFF"/>
          <stop offset="0.45" stop-color="#E8F1F8"/>
          <stop offset="1" stop-color="#D6E6F2"/>
        </linearGradient>
      </defs>
      <polygon points="0,0 366,0 336,320 0,320" fill="url(#mistFade)" role="img" aria-label="Large faint brand decoration"/>
      <polygon class="panel-navy" points="382,0 560,0 560,320 352,320"/>
      <polygon class="stripe-mid" points="366,0 371,0 341,320 336,320"/>
      <polygon class="stripe-deep" points="374,0 378,0 348,320 344,320"/>
    </svg>

    <div class="brand">
      <div class="brand-name">HARLOW RIDGE</div>
      <div class="brand-sub">CONSULTING</div>
    </div>

    <div class="contact">
      <div class="person-name">DANIEL REYES</div>
      <div class="person-role">President</div>
      <ul class="contact-list">
        <li>555-014-2738
          <svg viewBox="0 0 24 24"><path d="M6.6 10.8a15.1 15.1 0 0 0 6.6 6.6l2.2-2.2a1 1 0 0 1 1-.25 11.4 11.4 0 0 0 3.6.57 1 1 0 0 1 1 1V20a1 1 0 0 1-1 1A17 17 0 0 1 3 4a1 1 0 0 1 1-1h3.5a1 1 0 0 1 1 1c0 1.25.2 2.45.57 3.57a1 1 0 0 1-.25 1z"/></svg>
        </li>
        <li>daniel@harlowridge.com
          <svg viewBox="0 0 24 24"><path d="M2 5h20v14H2z"/><path d="M2 5l10 8 10-8" fill="none" stroke="#0A1220" stroke-width="2"/></svg>
        </li>
        <li>www.harlowridge.com
          <svg viewBox="0 0 24 24"><circle cx="12" cy="12" r="10"/></svg>
        </li>
      </ul>
    </div>
  </section>

</body>
</html>
```